I'm a fishing guide needing a clean, concise design for my business. I'd like to use the cover photo and font design from my website for the background of the business card. My website is:
www.brindlecoveoutfitters.net

Contact Information for Business Card

Capt. Owen Pelk
Fly, Light Tackle, Conventional Gear
Gamefish of Massachusetts
website: www.brindlecoveoutfitters.net
cell: 508-214-9072
email: owen@brindlecoveoutfitters.net

```html
<!DOCTYPE html>
<html lang="en">
<head>
<meta charset="utf-8">
<title>Brindle Cove Outfitters – Business Card</title>
<link rel="stylesheet" href="https://fonts.googleapis.com/css2?family=Questrial&family=Arimo:ital@0;1&display=swap">
<style>
  :root {
    --cream: #f2ead8;
    --white: #ffffff;
    --wave-red: #e8141b;
    --wave-blue: #1f3fe0;
    --ink: #111111;
    --accent-red: #e30d12;
    --mark-blue: #2a4fd8;
    --photo-dark: #2f3a55;
    --photo-mid: #5f6d8a;
    --photo-warm: #b98a8f;
  }
  html, body {
    margin: 0;
    padding: 0;
    width: 1200px;
    height: 741px;
    overflow: hidden;
    background: var(--cream);
  }
  .card {
    position: relative;
    width: 1200px;
    height: 741px;
    overflow: hidden;
    background: var(--cream);
    font-family: "Arimo", Arial, sans-serif;
    color: var(--ink);
  }
  .card-art {
    position: absolute;
    inset: 0;
  }
  .captain-name {
    position: absolute;
    left: 279px;
    top: 126px;
    margin: 0;
    font-family: "Questrial", "Century Gothic", sans-serif;
    font-weight: 400;
    font-size: 48px;
    letter-spacing: -1px;
    line-height: 1;
  }
  .specialty {
    position: absolute;
    left: 279px;
    top: 187px;
    margin: 0;
    font-family: "Arimo", Arial, sans-serif;
    font-style: italic;
    font-size: 24px;
    color: var(--accent-red);
    letter-spacing: -0.3px;
  }
  .contact-list {
    position: absolute;
    left: 192px;
    top: 229px;
    margin: 0;
    padding: 0;
    list-style: none;
    font-size: 27px;
    letter-spacing: -0.5px;
    line-height: 41px;
  }
  .contact-list .cell { font-size: 25px; }
  .brand-name {
    position: absolute;
    left: 50px;
    top: 580px;
    margin: 0;
    font-family: "Questrial", "Century Gothic", sans-serif;
    font-size: 54px;
    font-weight: 400;
    color: var(--white);
    letter-spacing: 1px;
  }
</style>
</head>
<body>
  <div class="card">
    <svg class="card-art" width="1200" height="741" viewBox="0 0 1200 741" aria-hidden="false">
      <defs>
        <linearGradient id="photoTone" x1="0" y1="0" x2="1" y2="0">
          <stop offset="0" stop-color="var(--photo-mid)"/>
          <stop offset="0.45" stop-color="var(--photo-dark)"/>
          <stop offset="0.8" stop-color="var(--photo-dark)"/>
          <stop offset="1" stop-color="var(--photo-warm)"/>
        </linearGradient>
      </defs>
      <rect class="background" width="1200" height="741" fill="var(--cream)"/>
      <rect class="cover-photo" x="25" y="400" width="1151" height="303" fill="url(#photoTone)"
            role="img" aria-label="Cover photo: close-up of a caught tuna's head with a colourful fly lure in its mouth"/>
      <path class="white-field" d="M0,0 H1200 V405 C800,380 350,445 0,440 Z" fill="var(--white)"/>
      <path class="top-wave-red" d="M0,95 C250,20 600,15 800,28 C600,30 300,50 0,135 Z" fill="var(--wave-red)"/>
      <path class="top-wave-blue" d="M30,125 C300,50 700,48 1200,30 V62 C800,58 350,92 35,152 Z" fill="var(--wave-blue)"/>
      <path class="bottom-wave-red" d="M560,368 C800,345 1050,360 1200,412 V440 C1050,395 800,376 560,368 Z" fill="var(--wave-red)"/>
      <path class="bottom-wave-blue" d="M0,432 C300,440 700,372 1200,398 V420 C800,396 350,462 0,458 Z" fill="var(--wave-blue)"/>
      <circle class="brand-dot" cx="150" cy="180" r="58" fill="var(--mark-blue)"/>
    </svg>

    <h1 class="captain-name">Capt. Owen Pelk Fly</h1>
    <p class="specialty">Light Tackle, Conventional Gear Gamefish of Massachusetts</p>
    <ul class="contact-list">
      <li class="cell">cell no.: 508-214-9072</li>
      <li class="email">email: owen@brindlecoveoutfitters.net</li>
      <li class="website">website: www.brindlecoveoutfitters.net</li>
    </ul>

    <p class="brand-name">Brindle Cove Outfitters</p>
  </div>
</body>
</html>
```